Werbematerial für Spendenaufruf
Zielgruppe
Wir betreuen Kinder im Alter von 6 Monaten bis zum Schuleintritt. Unsere Zielgruppe sind die Familien aus der Umgebung.
Es soll dieses Jahr ein neuer Naturkindergarten entstehen. Hierfür sammeln wir noch spenden.
Aufgabenstellung
Wir wollen einen Spendenaufruf starten für einen neuen Naturkindergarten, hier benötigen wir einen neuen Bauwagen für 23 Kinder und 3 Erwachsene.
Dieser Bauwagen soll möglichst mit Spenden finanziert werden.
Der Spendenaufruf soll auf den Social Media Accounts wie auch auf Flyern oder auf Werbeplakaten gedruckt werden.
Kosten für den Bauwagen liegen aktuell bei 130.000 Euro.
Die Kontodaten sollen hinzugefügt werden.

```html
<!DOCTYPE html>
<html lang="de">
<head>
<meta charset="utf-8">
<title>Spendenaufruf Naturkindergarten</title>
<link rel="stylesheet" href="https://fonts.googleapis.com/css2?family=Montserrat+Alternates:wght@500;800&family=Patrick+Hand+SC&display=swap">
<style>
  :root {
    --page: #e4e4e4;
    --white: #ffffff;
    --sky-teal: #8fc2bb;
    --shirt: #ef8a6a;
    --sun: #fff3c4;
    --grass-gold: #c98a2e;
    --sky-blue: #4f6fa8;
    --sky-light: #a9b9d6;
    --wood: #d2ad77;
    --grass-green: #6f9440;
    --shadow: rgba(0,0,0,.18);
  }
  * { margin: 0; padding: 0; box-sizing: border-box; }
  html, body { width: 1200px; height: 801px; overflow: hidden; background: var(--page); }
  .stage {
    position: relative; width: 1200px; height: 801px;
    display: flex; align-items: center; justify-content: center; gap: 40px;
  }
  .card {
    position: relative; width: 540px; height: 370px; overflow: hidden;
    box-shadow: 0 6px 18px var(--shadow);
  }
  .card__photo { position: absolute; inset: 0; }

  /* front */
  .card--front .card__photo {
    background:
      radial-gradient(circle at 72% 52%, var(--sun) 0%, rgba(255,230,150,.85) 12%, rgba(255,200,100,0) 38%),
      radial-gradient(ellipse at 42% 48%, var(--shirt) 0%, #e9775a 30%, rgba(233,119,90,0) 62%),
      linear-gradient(180deg, var(--sky-teal) 0%, #b9cfb0 42%, #e7b66a 60%, var(--grass-gold) 100%);
  }
  .front__kicker {
    position: absolute; left: 0; right: 0; top: 78px; text-align: center;
    font-family: "Patrick Hand SC", cursive; font-size: 22px; letter-spacing: 1px;
    color: var(--white); transform: rotate(-6deg);
  }
  .front__title {
    position: absolute; left: 0; right: 0; top: 98px; text-align: center;
    font-family: "Patrick Hand SC", cursive; font-size: 62px; font-weight: 400; letter-spacing: 2px;
    color: var(--white); transform: rotate(-6deg);
  }
  .front__wave { position: absolute; right: 14px; bottom: 72px; width: 160px; height: 70px; }
  .front__label {
    position: absolute; right: 118px; bottom: 36px;
    font-family: "Patrick Hand SC", cursive; font-size: 22px; letter-spacing: 1px;
    color: var(--white);
  }

  /* back */
  .card--back .card__photo {
    background:
      radial-gradient(circle at 90% 42%, var(--sun) 0%, rgba(255,220,140,.8) 8%, rgba(255,220,140,0) 26%),
      linear-gradient(180deg, var(--sky-blue) 0%, var(--sky-light) 42%, #c7b48d 55%, var(--grass-green) 66%, #5c7e35 100%);
  }
  .back__wagon {
    position: absolute; left: 140px; top: 162px; width: 330px; height: 78px;
    background: linear-gradient(180deg, #e1be88, var(--wood));
    border-top: 6px solid #c9ced4; border-radius: 4px;
  }
  .back__text {
    position: absolute; left: 0; right: 0; top: 14px; text-align: center;
    font-family: "Montserrat Alternates", sans-serif; color: var(--white);
    text-shadow: 0 1px 4px rgba(0,0,0,.25);
  }
  .back__title { font-size: 54px; font-weight: 500; letter-spacing: 3px; line-height: 1.05; }
  .back__sub { font-size: 17px; font-weight: 500; letter-spacing: 1px; }
  .back__amount { font-size: 34px; font-weight: 800; letter-spacing: 3px; margin-top: 2px; line-height: 1.2; }
  .back__contact {
    position: absolute; left: 200px; top: 258px;
    font-family: "Patrick Hand SC", cursive; font-size: 24px; letter-spacing: 1px;
    color: var(--white);
  }
  .back__arrow { position: absolute; left: 14px; bottom: 30px; width: 170px; height: 70px; }
</style>
</head>
<body>
<main class="stage">
  <section class="card card--front">
    <div class="card__photo" role="img" aria-label="Fotografie: lachendes Mädchen kopfüber auf einer Sommerwiese im Gegenlicht"></div>
    <p class="front__kicker">WIR PLANEN EINEN NEUEN</p>
    <h1 class="front__title">NATURKINDERGARTEN</h1>
    <svg class="front__wave" viewBox="0 0 160 70" aria-hidden="true">
      <path d="M8 58 C20 30, 40 20, 52 40 S78 70, 92 36 S130 10, 154 30" fill="none" stroke="var(--white)" stroke-width="14" stroke-linecap="round"/>
    </svg>
    <p class="front__label">SPENDENAUFRUF</p>
  </section>

  <section class="card card--back">
    <div class="card__photo" role="img" aria-label="Fotografie: Holz-Bauwagen auf einer Wiese bei Sonnenuntergang"></div>
    <div class="back__wagon" role="img" aria-label="Bauwagen aus Holz mit Treppe und Fenstern"></div>
    <div class="back__text">
      <h2 class="back__title">Bauwagen</h2>
      <p class="back__sub">für 23 Kinder und 3 Erwachsene</p>
      <p class="back__amount">130.000,- Euro</p>
    </div>
    <p class="back__contact">SPENDENKONTAKT:</p>
    <svg class="back__arrow" viewBox="0 0 170 70" aria-hidden="true">
      <path d="M8 40 C22 18, 40 26, 50 44 S80 62, 92 38 S122 16, 150 30" fill="none" stroke="var(--white)" stroke-width="12" stroke-linecap="round"/>
      <path d="M134 16 L156 30 L140 50" fill="none" stroke="var(--white)" stroke-width="12" stroke-linecap="round" stroke-linejoin="round"/>
    </svg>
  </section>
</main>
</body>
</html>
```